Yacht Management in Miami & Ft Lauderdale (2019Q2)

I’m looking for a flyer to leave places for people to get information about my company and what services we offer.
We offer monthly management plans to ensure the vessel is ready to go at a moments notice. This can be as simple as washing once a week, or as involved as washing, waxing, detailing, provisioning, and crew services.
We also offer bespoke customizations; stereos, on board WiFi, and engineering.

Target Market(s)

Yacht and boat owners.

Font styles to use
Sans Serif

Colors
87d0c7
85cae6
85acd3
cedeed
cee9f5
cfeae6
0455a3

Requirements
Must have
• Must have simple attention grabbing, without being obnoxious.
• Prefer a 3in x 5in post card size. other size may be an option.
• Must be front and back.
Nice to have
• Languages: English, Spanish, Russian
• USA flag logo
Should not have
• Should not have a lot of text. Icons and photos are great.

```html
<!DOCTYPE html>
<html lang="en">
<head>
<meta charset="utf-8">
<title>Harbor Sages – Postcard Front and Back</title>
<link href="https://fonts.googleapis.com/css2?family=Open+Sans:wght@300;400;600&display=swap" rel="stylesheet">
<style>
  :root {
    --page: #ffffff;
    --ink: #1b1d1f;
    --front-panel: #85acd3;
    --front-stripe: #a9c3e3;
    --front-field: #cedeed;
    --back-panel: #87d0c7;
    --back-stripe: #bfe4df;
    --back-field: #cfeae6;
    --rule: #a9d9d2;
    --label: #333333;
  }
  * { margin: 0; padding: 0; box-sizing: border-box; }
  html, body {
    width: 1200px; height: 800px; overflow: hidden;
    background: var(--page);
    font-family: "Open Sans", Arial, sans-serif;
    color: var(--ink);
  }
  .canvas { position: relative; width: 1200px; height: 800px; }

  .postcard {
    position: absolute; top: 208px;
    width: 523px; height: 314px; overflow: hidden;
  }
  .postcard--front { left: 67px; background: var(--front-field); }
  .postcard--back { left: 617px; background: var(--back-field); }

  .side-panel {
    position: absolute; left: 0; top: 0; width: 164px; height: 100%;
    text-align: center; font-weight: 300;
  }
  .postcard--front .side-panel { background: var(--front-panel); }
  .postcard--back .side-panel { background: var(--back-panel); }

  .side-stripe { position: absolute; left: 164px; top: 0; width: 13px; height: 100%; }
  .postcard--front .side-stripe { background: var(--front-stripe); }
  .postcard--back .side-stripe { background: var(--back-stripe); }

  .headline {
    position: absolute; left: 0; right: 0; top: 21px;
    font-size: 24px; line-height: 25px; font-weight: 300; letter-spacing: -0.3px;
  }
  .brand-name {
    position: absolute; left: 0; right: 0;
    font-size: 24px; line-height: 25px; font-weight: 600; letter-spacing: 1px;
    text-transform: uppercase;
  }
  .postcard--front .brand-name { top: 180px; }
  .postcard--back .brand-name { top: 226px; }

  .photo { position: absolute; }
  .photo--sky-band {
    left: 185px; top: 0; width: 338px; height: 20px;
    background: linear-gradient(90deg, #2c3444, #4a5263 60%, #3b4354);
  }
  .photo--deck { left: 185px; top: 26px; width: 107px; height: 65px;
    background: linear-gradient(160deg, #d9dcdf 0%, #a9a9a6 45%, #6a5c4c 100%); }
  .photo--salon { left: 297px; top: 26px; width: 107px; height: 65px;
    background: linear-gradient(180deg, #8b4a24 0%, #c98a56 35%, #e9ddca 70%, #b7a189 100%); }
  .photo--wake { left: 409px; top: 26px; width: 107px; height: 65px;
    background: linear-gradient(135deg, #a8bfd4 0%, #e6e1da 45%, #6c8cab 80%, #3f6486 100%); }
  .photo--night-marina { left: 185px; top: 96px; width: 338px; height: 218px;
    background: linear-gradient(180deg, #2f3847 0%, #5a6578 35%, #1f2326 62%, #1f5a2a 82%, #3fae3c 100%); }

  .contact {
    position: absolute; left: 0; right: 0;
    font-size: 13px; line-height: 14.5px; font-weight: 300; letter-spacing: -0.2px;
    white-space: nowrap;
  }
  .contact--web { top: 90px; }
  .contact--phone { top: 113px; }
  .contact--address { top: 150px; }

  .photo--back-sky {
    left: 185px; top: 0; width: 338px; height: 24px;
    background: linear-gradient(90deg, #3f4a55, #6c7580 70%, #9aa0a6);
  }
  .service-list {
    position: absolute; left: 185px; top: 24px; width: 338px; height: 152px;
    list-style: none; padding: 4px 20px 0 10px;
  }
  .service-item {
    display: flex; align-items: center; height: 29px;
    border-bottom: 1px solid var(--rule);
    font-size: 13.6px; font-weight: 300; letter-spacing: -0.1px; white-space: nowrap;
  }
  .service-item:last-child { border-bottom: none; }
  .service-icon { width: 30px; height: 20px; margin-right: 8px; flex: none; }
  .photo--sunset {
    left: 185px; top: 176px; width: 338px; height: 138px;
    background: linear-gradient(180deg, #8e8578 0%, #e9a84a 22%, #3d4048 32%, #55585d 55%, #b7b3ad 78%, #8d8a86 100%);
  }

  .side-label {
    position: absolute; top: 757px; font-size: 10.5px; font-weight: 400; color: var(--label);
  }
  .side-label--front { right: 610px; }
  .side-label--back { left: 617px; }
  .side-divider {
    position: absolute; left: 603px; top: 741px; width: 1px; height: 49px; background: var(--label);
  }
</style>
</head>
<body>
<main class="canvas">

  <section class="postcard postcard--front" aria-label="Postcard front">
    <div class="side-panel">
      <h1 class="headline">Complete<br>yacht service<br>you can trust</h1>
      <p class="brand-name">Harbor<br>Sages</p>
    </div>
    <div class="side-stripe"></div>
    <div class="photo photo--sky-band" role="img" aria-label="Dusky evening sky"></div>
    <div class="photo photo--deck" role="img" aria-label="Teak side deck of a yacht"></div>
    <div class="photo photo--salon" role="img" aria-label="Yacht salon interior with sofas and wood ceiling"></div>
    <div class="photo photo--wake" role="img" aria-label="Yacht hull cruising over open water"></div>
    <div class="photo photo--night-marina" role="img" aria-label="Motor yacht docked at night with green underwater lights and city skyline"></div>
  </section>

  <section class="postcard postcard--back" aria-label="Postcard back">
    <div class="side-panel">
      <h2 class="headline">Contact us to<br>find out more</h2>
      <p class="contact contact--web">harborsage.co</p>
      <p class="contact contact--phone">call: (305) 555-0142<br>email: info@harborsage.co</p>
      <p class="contact contact--address">880 Bayview Lane, #210<br>Coral Bay, FL 33100</p>
      <p class="brand-name">Harbor<br>Sages</p>
    </div>
    <div class="side-stripe"></div>
    <div class="photo photo--back-sky" role="img" aria-label="Cloudy sky over the water"></div>

    <ul class="service-list">
      <li class="service-item">
        <svg class="service-icon" viewBox="0 0 30 20" aria-hidden="true">
          <g fill="none" stroke="#1b1d1f" stroke-width="1.6" stroke-linecap="round">
            <circle cx="15" cy="3" r="1.8"/><line x1="15" y1="5" x2="15" y2="18"/>
            <line x1="11" y1="8" x2="19" y2="8"/><path d="M8 12 Q9 18 15 18 Q21 18 22 12"/>
          </g>
        </svg>
        Yacht service &amp; monthly management plans
      </li>
      <li class="service-item">
        <svg class="service-icon" viewBox="0 0 30 20" aria-hidden="true">
          <g fill="#1b1d1f">
            <rect x="13" y="1" width="4" height="4"/><rect x="10" y="5" width="10" height="5"/>
            <path d="M6 10 H24 L21 18 H9 Z"/>
          </g>
        </svg>
        Bespoke refits, updates &amp; customizations
      </li>
      <li class="service-item">
        <svg class="service-icon" viewBox="0 0 30 20" aria-hidden="true">
          <rect x="10" y="1" width="10" height="18" rx="1.5" fill="#1b1d1f"/>
          <circle cx="15" cy="6" r="2" fill="#cfeae6"/><circle cx="15" cy="13" r="3" fill="#cfeae6"/>
          <g fill="none" stroke="#1b1d1f" stroke-width="1.5">
            <path d="M7 6 Q5 10 7 14"/><path d="M4 4 Q1 10 4 16"/>
            <path d="M23 6 Q25 10 23 14"/><path d="M26 4 Q29 10 26 16"/>
          </g>
        </svg>
        Audio-visual packages &amp; on-board wi-fi
      </li>
      <li class="service-item">
        <svg class="service-icon" viewBox="0 0 30 20" aria-hidden="true">
          <ellipse cx="15" cy="10" rx="13" ry="7" fill="#1b1d1f"/>
          <path d="M5 11 Q15 6 25 11" fill="none" stroke="#cfeae6" stroke-width="1.5"/>
          <circle cx="15" cy="7" r="1.5" fill="#cfeae6"/>
        </svg>
        Captaining and crew services
      </li>
      <li class="service-item">
        <svg class="service-icon" viewBox="0 0 30 20" aria-hidden="true">
          <rect x="3" y="1" width="24" height="15" fill="none" stroke="#1b1d1f" stroke-width="1.6"/>
          <path d="M11 9 L14 12 L19 5" fill="none" stroke="#1b1d1f" stroke-width="1.5"/>
          <path d="M12 16 H18 L19 19 H11 Z" fill="#1b1d1f"/>
        </svg>
        Internet sales for DIY installations
      </li>
    </ul>

    <div class="photo photo--sunset" role="img" aria-label="Yacht bow at sunset over calm sea"></div>
  </section>

  <span class="side-label side-label--front">FRONT</span>
  <span class="side-divider"></span>
  <span class="side-label side-label--back">BACK</span>

</main>
</body>
</html>
```